Tallowmere Contracting Business Cards

Front of card:

Full Logo
Name
Address
Office Phone
Cell Phone
Email
Website

Back:
Logo Mark in background
List and markets and services performed

```html
<!DOCTYPE html>
<html lang="en">
<head>
<meta charset="utf-8">
<title>Tallowmere Contracting Business Cards</title>
<link rel="stylesheet" href="https://fonts.googleapis.com/css2?family=Arimo:wght@400;700&display=swap">
<style>
  :root {
    --backdrop: #3b3b3b;
    --card: #0d0d0d;
    --red: #e0262b;
    --grey: #8a8a8a;
    --light: #e9e9e9;
    --rule: #5a5a5a;
  }
  * { box-sizing: border-box; margin: 0; padding: 0; }
  html, body { width: 1200px; height: 959px; overflow: hidden; }
  body {
    background: var(--backdrop);
    font-family: "Arimo", Arial, sans-serif;
    position: relative;
  }
  .card {
    position: absolute;
    width: 560px;
    height: 320px;
    background: var(--card);
    border-radius: 18px;
  }
  .card-back { left: 320px; top: 100px; }
  .card-front { left: 320px; top: 520px; }

  /* Back */
  .back-mark {
    position: absolute;
    left: 50%; top: 70px;
    transform: translateX(-50%);
    width: 110px; height: 110px;
    border-radius: 50%;
    border: 10px solid var(--red);
  }
  .back-tagline {
    position: absolute;
    left: 0; right: 0; top: 210px;
    text-align: center;
    color: var(--red);
    font-size: 15px;
  }

  /* Front */
  .brand {
    position: absolute;
    left: 40px; top: 140px;
    display: flex; align-items: center; gap: 14px;
  }
  .brand-dot {
    width: 46px; height: 46px;
    border-radius: 50%;
    background: var(--red);
  }
  .brand-name {
    color: var(--red);
    font-weight: 700;
    font-size: 20px;
    letter-spacing: 0.5px;
    text-transform: uppercase;
    line-height: 1.15;
  }
  .divider {
    position: absolute;
    left: 290px; top: 60px;
    width: 1px; height: 200px;
    background: var(--rule);
  }
  .contact {
    position: absolute;
    left: 312px; top: 62px;
    color: var(--light);
    font-size: 12.5px;
    line-height: 1.45;
  }
  .person-name {
    font-size: 22px;
    text-transform: uppercase;
    line-height: 1.1;
  }
  .person-name .first { color: var(--red); }
  .person-name .last { color: var(--grey); }
  .person-role { margin-bottom: 12px; }
  .address { margin-bottom: 12px; }
  .contact-list { list-style: none; }
  .contact-list li { display: flex; align-items: center; gap: 6px; }
  .contact-list svg { width: 11px; height: 11px; flex: none; }
</style>
</head>
<body>
  <section class="card card-back" aria-label="Card back">
    <div class="back-mark" aria-hidden="true"></div>
    <p class="back-tagline">List and markets and services performed</p>
  </section>

  <section class="card card-front" aria-label="Card front">
    <div class="brand">
      <span class="brand-dot" aria-hidden="true"></span>
      <span class="brand-name">Tallowmere<br>Contracting</span>
    </div>

    <div class="divider" aria-hidden="true"></div>

    <div class="contact">
      <p class="person-name"><span class="first">Daniel</span> <span class="last">Morrow</span></p>
      <p class="person-role">Founder</p>
      <p class="address">42 Harlow Avenue, Ground Floor<br>Brookfield, NY 10450</p>
      <ul class="contact-list">
        <li>
          <svg viewBox="0 0 12 12" aria-hidden="true"><path d="M2 1l2.5 0 1 3-1.5 1a7 7 0 0 0 3 3l1-1.5 3 1V11C6 11 1 6 1 2z" fill="#e0262b"/></svg>
          (555) 201-4470
        </li>
        <li>
          <svg viewBox="0 0 12 12" aria-hidden="true"><rect x="3" y="1" width="6" height="10" rx="1" fill="none" stroke="#e0262b" stroke-width="1.3"/></svg>
          (555) 201-4472
        </li>
        <li>
          <svg viewBox="0 0 12 12" aria-hidden="true"><rect x="1" y="2.5" width="10" height="7" fill="#e0262b"/><path d="M1 2.5l5 4 5-4" fill="none" stroke="#0d0d0d" stroke-width="1"/></svg>
          info@TallowmereContractingllc.com
        </li>
        <li>
          <svg viewBox="0 0 12 12" aria-hidden="true"><circle cx="6" cy="6" r="5" fill="none" stroke="#e0262b" stroke-width="1.2"/><path d="M1 6h10M6 1c-2.5 3-2.5 7 0 10M6 1c2.5 3 2.5 7 0 10" fill="none" stroke="#e0262b" stroke-width="0.9"/></svg>
          www.TallowmereContractingllc.com
        </li>
      </ul>
    </div>
  </section>
</body>
</html>
```